Powerpoint template for basic scientists studying immunology

We are an QVA-funded consortium of basic science researchers at academic centers in Boston, Philadelphia and Oxford, UK. We study why the immune system fails to get rid of Hepatitis C virus, and whether new antiviral treatments that reduce viral load improve immune function. We are looking for a powerpoint template that we can use as a "brand" for our research consortium. It would feature a logo (file attached) and should represent the fonts/colors contained in the logo. We we would present at meetings and to program officers at the QVA, but, if we ever get around to it, would also be on a website.

The scientific description is as follows:
Hepatitis C virus (HCV) infects 185 million persons worldwide, is the leading indication for liver transplantation and, in the US, has a higher mortaliy rate than HIV. The annual healthcare costs associated with HCV exceed $9 billion, a number expected to increase as the epidemic matures and end stage liver disease peaks over the next decade. By virtue of its remarkable predilection for persistence, HCV is a model chronic viral infection. Mounting evidence supports the idea that HCV, while inducing type I IFN expression, maintains chronicity by virtue of global suppression of host innate and adaptive immunity. The mainstay of treatment for the last two decades, IFN-α-based regimens are ineffective in many patient subgroups and have significant side effects. The recent development of highly effective direct acting antivirals (DAA) against HCV promises to alter the landscape of this devastating infection by offering curative therapy without IFN. However, it remains essential that we understand what type of immunity remains following pharmacological eradication of the virus because: a) many HCV infected subjects remain at risk for re-infection; and b) DAAs are only partially effective in some patient subgroups, particularly those with past treatment with IFN. The imminent availability of IFN-free treatment for HCV offers an unprecedented opportunity to understand broad questions about alterations in immunity in humans with cure of chronic infections. Until now, mechanistic dissection of human immune responses has been challenging due to limited ability to directly perturb the system. The organizing principle of this U19 Program therefore, is to capitalize on the unique opportunity to, for the first time, cure chronic viral infection in humans without immune modulation and interrogate the immunological changes that ensue. Thus, we have formulated the following central hypothesis for this Program: DAA-mediated cure of chronic HCV infection will lead to partial "resetting" of some immune abnormalities, but specific immunological defects will persist in some subjects that prevent development of optimal immunity to HCV. We will test this hypothesis through a set of integrated Projects and Cores.

Target Market(s)

scientists.

Industry/Entity Type

Biotechnology

Font styles to use
Sans Serif

Requirements
Must have
• Very clean, very simple. Mostly whitespace for puting graphs and data on. Colors, fonts should match the logo. Please see ppt example.
Should not have
• too much of the ppt covered with the logo.

```html
<!DOCTYPE html>
<html lang="en">
<head>
<meta charset="utf-8">
<title>Meridane – Slide Template</title>
<link rel="stylesheet" href="https://fonts.googleapis.com/css2?family=Arimo:wght@400;700&display=swap">
<style>
  :root {
    --frame: #3b3b3b;
    --paper: #ffffff;
    --brand-blue: #1b9fd9;
    --brand-green: #78b843;
    --text-grey: #6a6a6a;
    --body-grey: #595959;
    --rule: #8c8c8c;
    --grid: #d9d9d9;
    --axis: #a6a6a6;
    --series-1: #4f81bd;
    --series-2: #c0504d;
    --series-3: #9bbb59;
  }
  * { box-sizing: border-box; margin: 0; padding: 0; }
  html, body { width: 1200px; height: 900px; overflow: hidden; }
  body {
    background: var(--frame);
    font-family: "Arimo", Arial, sans-serif;
    position: relative;
  }
  .slide {
    position: absolute;
    width: 588px;
    height: 443px;
    background: var(--paper);
    overflow: hidden;
  }
  .slide--title    { left: 0;     top: 0; }
  .slide--question { left: 612px; top: 0; }
  .slide--bullets  { left: 0;     top: 457px; }
  .slide--charts   { left: 612px; top: 457px; }

  .brand-band {
    position: absolute; left: 0; right: 0; bottom: 0; height: 15px;
    background: linear-gradient(to right, var(--brand-blue) 0 119px, var(--brand-green) 119px);
  }
  .brand-mark {
    position: absolute; right: 22px; bottom: 30px;
    display: flex; align-items: center; gap: 5px;
    color: var(--brand-blue); font-size: 10px; font-weight: 400; letter-spacing: .3px;
  }
  .brand-mark__dot { width: 12px; height: 12px; border-radius: 50%; background: var(--brand-green); }

  /* Title slide */
  .cover__title {
    position: absolute; left: 79px; top: 132px;
    color: var(--brand-blue); font-size: 24px; font-weight: 700; letter-spacing: .2px;
  }
  .cover__rule {
    position: absolute; left: 69px; top: 164px; width: 399px; height: 1px; background: var(--rule);
  }
  .cover__details {
    position: absolute; left: 79px; top: 188px;
    color: var(--text-grey); font-size: 13.5px; line-height: 17px;
  }
  .cover__details p + p { margin-top: 17px; }

  /* Question slide */
  .question {
    position: absolute; left: 64px; top: 130px;
    color: var(--text-grey); font-size: 32px; line-height: 40px;
  }
  .accent-green { color: var(--brand-green); }
  .accent-blue { color: var(--brand-blue); }

  /* Content slides */
  .slide__title {
    position: absolute; left: 64px; top: 36px;
    color: var(--brand-blue); font-size: 27px; font-weight: 700; letter-spacing: .2px;
  }
  .slide__subtitle {
    position: absolute; left: 64px; top: 72px; width: 450px;
    color: var(--text-grey); font-size: 21.5px; line-height: 28px;
  }
  .bullet-list {
    position: absolute; left: 70px; top: 163px; width: 456px;
    list-style: none; color: var(--body-grey); font-size: 13.5px; line-height: 17.5px;
  }
  .bullet-list li { position: relative; padding-left: 15px; }
  .bullet-list li + li { margin-top: 17.5px; }
  .bullet-list li::before {
    content: ""; position: absolute; left: 0; top: 6px; width: 4px; height: 4px; background: var(--brand-green);
  }
  .chart-set { position: absolute; left: 0; top: 0; }
  .chart-caption {
    position: absolute; top: 338px; width: 210px;
    color: var(--text-grey); font-size: 13px; line-height: 17px;
  }
  .chart-caption--line { left: 62px; }
  .chart-caption--bar { left: 325px; }
  .axis-label { font-family: "Arimo", Arial, sans-serif; font-size: 9px; fill: #595959; }
  .legend-label { font-family: "Arimo", Arial, sans-serif; font-size: 10px; fill: #595959; }
</style>
</head>
<body>

<section class="slide slide--title">
  <h1 class="cover__title">PRESENTATION TITLE</h1>
  <div class="cover__rule"></div>
  <div class="cover__details">
    <p>Elena Marsh, B.M., B.Ch.</p>
    <p>Assistant Professor of Pediatrics<br>Northfield Cancer Institute<br>Ashbury Medical School</p>
    <p>Associate Member<br>Lindqvist Institute of Ashbury and Bayview</p>
  </div>
  <div class="brand-mark"><span class="brand-mark__dot"></span>Meridane</div>
  <div class="brand-band"></div>
</section>

<section class="slide slide--question">
  <p class="question">
    What does <span class="accent-green">BATF</span> do<br>
    that makes it so important<br>
    for <span class="accent-green">CD8 effector differentiation?</span><br>
    <span class="accent-blue">2 color text for more emphasis</span>
  </p>
  <div class="brand-mark"><span class="brand-mark__dot"></span>Meridane</div>
  <div class="brand-band"></div>
</section>

<section class="slide slide--bullets">
  <h2 class="slide__title">PRESENTATION TITLE</h2>
  <p class="slide__subtitle">Another text title as needed as needed as needed</p>
  <ul class="bullet-list">
    <li>Lorem ipsum dolor sit amet, consectetuer adipiscing elit. Maecenas porttitor congue massa. Fusce posuere, magna sed pulvinar ultricies, purus lectus malesuada libero, sit amet commodo magna eros quis urna.</li>
    <li>Lorem ipsum dolor sit amet, consectetuer adipiscing elit. Maecenas porttitor congue massa. Fusce posuere, magna sed pulvinar ultricies, purus lectus malesuada libero, sit amet commodo magna eros quis urna.</li>
  </ul>
  <div class="brand-mark"><span class="brand-mark__dot"></span>Meridane</div>
  <div class="brand-band"></div>
</section>

<section class="slide slide--charts">
  <h2 class="slide__title">PRESENTATION TITLE</h2>
  <p class="slide__subtitle">Another text title as needed as needed as needed</p>

  <svg class="chart-set" width="588" height="443" viewBox="0 0 588 443" aria-label="Line chart and bar chart of three series">
    <g class="chart chart--line">
      <g stroke="var(--grid)" stroke-width="1">
        <line x1="80" x2="180" y1="149" y2="149"/><line x1="80" x2="180" y1="172.3" y2="172.3"/>
        <line x1="80" x2="180" y1="195.7" y2="195.7"/><line x1="80" x2="180" y1="219" y2="219"/>
        <line x1="80" x2="180" y1="242.3" y2="242.3"/><line x1="80" x2="180" y1="265.7" y2="265.7"/>
      </g>
      <line x1="80" x2="180" y1="289" y2="289" stroke="var(--axis)"/>
      <g class="axis-label" text-anchor="end">
        <text x="73" y="292">0</text><text x="73" y="268.7">1</text><text x="73" y="245.3">2</text>
        <text x="73" y="222">3</text><text x="73" y="198.7">4</text><text x="73" y="175.3">5</text><text x="73" y="152">6</text>
      </g>
      <g class="axis-label" text-anchor="middle">
        <text x="92.5" y="304">1</text><text x="117.5" y="304">2</text><text x="142.5" y="304">3</text><text x="167.5" y="304">4</text>
      </g>
      <g fill="none" stroke-width="2">
        <polyline stroke="var(--series-1)" points="92.5,188.7 117.5,230.7 142.5,207.3 167.5,184"/>
        <polyline stroke="var(--series-2)" points="92.5,233 117.5,186.3 142.5,247 167.5,223.7"/>
        <polyline stroke="var(--series-3)" points="92.5,242.3 117.5,242.3 142.5,219 167.5,172.3"/>
      </g>
      <g stroke-width="2">
        <line x1="205" x2="222" y1="205" y2="205" stroke="var(--series-1)"/>
        <line x1="205" x2="222" y1="225" y2="225" stroke="var(--series-2)"/>
        <line x1="205" x2="222" y1="245" y2="245" stroke="var(--series-3)"/>
      </g>
      <g class="legend-label">
        <text x="226" y="208.5">Series 1</text><text x="226" y="228.5">Series 2</text><text x="226" y="248.5">Series 3</text>
      </g>
    </g>

    <g class="chart chart--bar">
      <g stroke="var(--grid)" stroke-width="1">
        <line x1="314" x2="425" y1="149" y2="149"/><line x1="314" x2="425" y1="172.3" y2="172.3"/>
        <line x1="314" x2="425" y1="195.7" y2="195.7"/><line x1="314" x2="425" y1="219" y2="219"/>
        <line x1="314" x2="425" y1="242.3" y2="242.3"/><line x1="314" x2="425" y1="265.7" y2="265.7"/>
      </g>
      <g class="axis-label" text-anchor="end">
        <text x="307" y="292">0</text><text x="307" y="268.7">1</text><text x="307" y="245.3">2</text>
        <text x="307" y="222">3</text><text x="307" y="198.7">4</text><text x="307" y="175.3">5</text><text x="307" y="152">6</text>
      </g>
      <g class="axis-label" text-anchor="middle">
        <text x="327.9" y="304">1</text><text x="355.6" y="304">2</text><text x="383.4" y="304">3</text><text x="411.1" y="304">4</text>
      </g>
      <g fill="var(--series-1)">
        <rect x="318.1" y="188.7" width="6.5" height="100.3"/><rect x="345.9" y="230.7" width="6.5" height="58.3"/>
        <rect x="373.6" y="207.3" width="6.5" height="81.7"/><rect x="401.4" y="184" width="6.5" height="105"/>
      </g>
      <g fill="var(--series-2)">
        <rect x="324.6" y="233" width="6.5" height="56"/><rect x="352.4" y="186.3" width="6.5" height="102.7"/>
        <rect x="380.1" y="247" width="6.5" height="42"/><rect x="407.9" y="223.7" width="6.5" height="65.3"/>
      </g>
      <g fill="var(--series-3)">
        <rect x="331.1" y="242.3" width="6.5" height="46.7"/><rect x="358.9" y="242.3" width="6.5" height="46.7"/>
        <rect x="386.6" y="219" width="6.5" height="70"/><rect x="414.4" y="172.3" width="6.5" height="116.7"/>
      </g>
      <line x1="314" x2="425" y1="289" y2="289" stroke="var(--axis)"/>
      <rect x="480" y="201" width="7" height="7" fill="var(--series-1)"/>
      <rect x="480" y="221" width="7" height="7" fill="var(--series-2)"/>
      <rect x="480" y="241" width="7" height="7" fill="var(--series-3)"/>
      <g class="legend-label">
        <text x="492" y="208.5">Series 1</text><text x="492" y="228.5">Series 2</text><text x="492" y="248.5">Series 3</text>
      </g>
    </g>
  </svg>

  <p class="chart-caption chart-caption--line">Another text title as needed as needed as needed</p>
  <p class="chart-caption chart-caption--bar">Another text title as needed as needed as needed</p>

  <div class="brand-mark"><span class="brand-mark__dot"></span>Meridane</div>
  <div class="brand-band"></div>
</section>

</body>
</html>
```